Innovative Australian Importation company in Sustainability space needs beautiful website*

We seek your services to provide a clean, modern we rendered logo for or company Ferntide Commerce Imports Pty Ltd, this will be used in all the usual places however you will aso build us our business cards and our website: ferntidecommerceimports.example

What we do:
We source innovative products that solve problems in the Aeroponics, Hydroponics, Horticultural, Organics and sustainability space. We source our product from all over the world however our cliant base is predominantly in Australia & New Zealand Region.
Our company's mission is to help retail businesses by providing high-quality products at a competitive price for everyday people to produce healthy sustainable consumables from home, making it easy for the end-user to become more self-sufficient with while remaining environmentally friendly.

Target Market(s)

Aeroponics, Hydroponics, Horticultural, Organics and sustainability space.

Industry/Entity Type

Wholesale

Contact Information for Business Card

We would like these to be very modern and glossy possibly an embosed logo or rounded edges, a little smaller than the traditional?

Logo Text

Ferntide Commerce Imports

Coding

Coded - Design and coding required

Number of Pages Required

1 page

Colors
0355a3

Requirements
Must have
• The websit is bit of a landing page that will provide some minor information on our imported products. and qualify resellers ( Our target Market) from retail clients (the end-user) and provide a private store and check out for our trade customers. (not for Reatil)
Abillity to set up a trade account (must have our approval befor being granted access to shop.)
the abillity to for OEM's and International wholsalers register intrest.
The abillity to register/inquire about our produtc lines for Retailer.
The abillity to provide the end-user a list of resellers.
The ability for promo video
Nice to have
• .
Should not have
• Logo high gloss, 3d rendered

```html
<!DOCTYPE html>
<html lang="en">
<head>
<meta charset="utf-8">
<title>Ferntide Commerce Imports – Business Cards</title>
<link href="https://fonts.googleapis.com/css2?family=Roboto:wght@400;500;700&display=swap" rel="stylesheet">
<style>
  :root {
    --backdrop-top: #e6e6e6;
    --backdrop-bottom: #ffffff;
    --card-black: #000000;
    --brand-blue: #0355a3;
    --brand-sky: #2f8fe0;
    --brand-green: #22cc6a;
    --text-white: #ffffff;
  }
  * { box-sizing: border-box; margin: 0; padding: 0; }
  html, body { width: 1016px; height: 1200px; overflow: hidden; }
  body {
    font-family: "Roboto", Arial, sans-serif;
    background: linear-gradient(180deg, var(--backdrop-top) 0%, var(--backdrop-bottom) 55%);
    position: relative;
  }
  .card {
    position: absolute;
    left: 97px;
    width: 821px;
    height: 467px;
    background: var(--card-black);
    border-radius: 0 72px 0 72px;
    overflow: hidden;
  }
  .card--front { top: 100px; }
  .card--back { top: 628px; }
  .card__waves { position: absolute; inset: 0; width: 100%; height: 100%; }

  .brand-mark {
    position: absolute;
    border-radius: 50%;
    background: radial-gradient(circle at 45% 40%, var(--brand-sky), var(--brand-blue));
  }
  .brand-name {
    position: absolute;
    color: var(--brand-sky);
    font-weight: 700;
    text-transform: uppercase;
    letter-spacing: 0.08em;
    line-height: 1.25;
  }

  /* front */
  .card--front .brand-mark { left: 78px; top: 115px; width: 150px; height: 150px; }
  .card--front .brand-name { left: 254px; top: 138px; font-size: 40px; }
  .front-contacts {
    position: absolute;
    left: 0; right: 0; top: 418px;
    display: flex; justify-content: center; gap: 58px;
    color: var(--text-white); font-size: 20px;
  }
  .front-contacts__item { display: flex; align-items: center; gap: 12px; white-space: nowrap; }
  .front-contacts__item svg { width: 20px; height: 20px; fill: var(--text-white); }

  /* back */
  .card--back .brand-mark { left: 139px; top: 75px; width: 140px; height: 140px; }
  .card--back .brand-name { left: 20px; width: 382px; top: 228px; font-size: 25px; text-align: center; }
  .person {
    position: absolute; left: 384px; top: 42px;
    color: var(--brand-green); font-size: 27px;
  }
  .person__role { font-size: 19px; }
  .contact-list { position: absolute; left: 384px; top: 108px; width: 420px; list-style: none; }
  .contact-list__item {
    display: flex; align-items: flex-start; gap: 16px;
    color: var(--text-white); font-size: 22px; line-height: 1.45;
    margin-bottom: 31px;
  }
  .contact-list__icon {
    flex: none; width: 42px; height: 42px;
    border: 2px solid var(--brand-green); border-radius: 50%;
    display: flex; align-items: center; justify-content: center;
  }
  .contact-list__icon svg { width: 20px; height: 20px; fill: var(--brand-green); }
  .contact-list__text { padding-top: 5px; white-space: nowrap; }
  .contact-list__text--email { font-size: 18px; padding-top: 8px; }
  .sectors {
    position: absolute; left: 0; right: 0; top: 418px;
    text-align: center; color: var(--text-white);
    font-size: 19px; font-weight: 500; word-spacing: 2px;
  }
</style>
</head>
<body>

<section class="card card--front" aria-label="Business card front">
  <svg class="card__waves" viewBox="0 0 821 467" preserveAspectRatio="none" aria-hidden="true">
    <path d="M0 355 C140 348 290 362 420 392 L821 392 L821 467 L0 467 Z" fill="var(--brand-green)"/>
    <path d="M0 405 C200 375 300 395 480 392 C640 390 740 380 821 366 L821 467 L0 467 Z" fill="var(--brand-blue)"/>
  </svg>
  <div class="brand-mark"></div>
  <div class="brand-name">Ferntide Commerce<br>Imports</div>
  <div class="front-contacts">
    <span class="front-contacts__item">
      <svg viewBox="0 0 24 24"><path d="M3 2h18a1 1 0 0 1 1 1v18a1 1 0 0 1-1 1H3a1 1 0 0 1-1-1V3a1 1 0 0 1 1-1zm4.5 4C7 6 6 7 6 8c0 5 5 10 10 10 1 0 2-1 2-1.5l-2.5-2-1.5 1.2c-2-1-3.5-2.5-4.5-4.5L10.7 9.7 8.5 6z"/></svg>
      1300 482 917
    </span>
    <span class="front-contacts__item">
      <svg viewBox="0 0 24 24"><path d="M2 5h20v2l-10 6L2 7zm0 4l10 6 10-6v10H2z"/></svg>
      hello@ferntidecommerceimports.example
    </span>
  </div>
</section>

<section class="card card--back" aria-label="Business card back">
  <svg class="card__waves" viewBox="0 0 821 467" preserveAspectRatio="none" aria-hidden="true">
    <path d="M280 410 C460 362 640 362 821 374 L821 467 L280 467 Z" fill="var(--brand-green)"/>
    <path d="M0 372 C150 360 260 395 420 408 C580 418 720 410 821 414 L821 467 L0 467 Z" fill="var(--brand-blue)"/>
  </svg>
  <div class="brand-mark"></div>
  <div class="brand-name">Ferntide Commerce<br>Imports</div>
  <p class="person">Mara Ellison, <span class="person__role">Sales Manager</span></p>
  <ul class="contact-list">
    <li class="contact-list__item">
      <span class="contact-list__icon"><svg viewBox="0 0 24 24"><path d="M2 5h20v2l-10 6L2 7zm0 4l10 6 10-6v10H2z"/></svg></span>
      <span class="contact-list__text contact-list__text--email">sales@ferntidecommerceimports.example</span>
    </li>
    <li class="contact-list__item">
      <span class="contact-list__icon"><svg viewBox="0 0 24 24"><path d="M6.6 10.8c1.4 2.8 3.8 5.2 6.6 6.6l2.2-2.2c.3-.3.7-.4 1-.2 1.1.4 2.3.6 3.6.6.6 0 1 .4 1 1V20c0 .6-.4 1-1 1C10.6 21 3 13.4 3 4c0-.6.4-1 1-1h3.5c.6 0 1 .4 1 1 0 1.3.2 2.5.6 3.6.1.3 0 .7-.2 1z"/></svg></span>
      <span class="contact-list__text">1300 482 917</span>
    </li>
    <li class="contact-list__item">
      <span class="contact-list__icon"><svg viewBox="0 0 24 24"><path d="M12 2a7 7 0 0 0-7 7c0 5.2 7 13 7 13s7-7.8 7-13a7 7 0 0 0-7-7zm0 9.5A2.5 2.5 0 1 1 12 6.5a2.5 2.5 0 0 1 0 5z"/></svg></span>
      <span class="contact-list__text">Po Box 5820<br>Kelvin Grove BC<br>Queensland 4059</span>
    </li>
  </ul>
  <p class="sectors">Aeroponics &nbsp;|&nbsp; Hydroponics &nbsp;|&nbsp; Horticultural &nbsp;|&nbsp; Organics &nbsp;|&nbsp; Sustainability Space</p>
</section>

</body>
</html>
```